Author and Publisher

Cover for a book on the process of publishing a book from the presentation to the publisher until the selling in bookstores :
A behind-the-scenes journey through the world of book publishing, from manuscript to bookstore. The book explores the relationship between authors and publishers, manuscript selection, contracts, editing, proofreading, book design, printing, distribution, bookstores and online sales. It reveals the many people, decisions and processes involved in turning a text into a physical book and bringing it to readers. The illustration should evoke publishing as a lively, contemporary ecosystem, combining creativity, craftsmanship, business and the enduring appeal of books.
FORMAT : 14 x 20,5 cm
AUTHOR : Luc Dorvasse
TITLE : Le veilleur et la rive
PUBLISHER : Editions Plumeaux (at the bottom of the page)
Target Market(s)
General public, mainly news authors of books
Look and feel

```html
<!DOCTYPE html>
<html lang="fr">
<head>
<meta charset="utf-8">
<title>Le veilleur et la rive — Luc Dorvasse</title>
<link href="https://fonts.googleapis.com/css2?family=Lato:wght@400;700&family=Special+Elite&display=swap" rel="stylesheet">
<style>
  :root {
    --paper-white: #fdfdfd;
    --ink-black: #161412;
    --sepia-light: #f3e9df;
    --sepia-mid: #cdb39d;
    --sepia-dark: #2a1d14;
    --type-ink: #2b211b;
    --footer-band: #f0e5de;
  }
  * { margin: 0; padding: 0; box-sizing: border-box; }
  html, body {
    width: 820px;
    height: 1200px;
    overflow: hidden;
    background: var(--paper-white);
  }
  .cover {
    position: relative;
    width: 820px;
    height: 1200px;
    overflow: hidden;
    background: var(--paper-white);
  }
  .author-band {
    position: absolute;
    top: 0; left: 0;
    width: 820px;
    height: 198px;
    display: flex;
    align-items: center;
    justify-content: center;
    padding-bottom: 4px;
  }
  .author-name {
    font-family: "Lato", sans-serif;
    font-weight: 700;
    font-size: 44px;
    letter-spacing: 3px;
    text-transform: uppercase;
    color: var(--ink-black);
  }
  .typewriter-photo {
    position: absolute;
    top: 198px; left: 0;
    width: 820px;
    height: 912px;
    background:
      radial-gradient(ellipse 520px 300px at 140px 860px, var(--sepia-dark) 0%, rgba(42,29,20,0.75) 45%, rgba(42,29,20,0) 100%),
      linear-gradient(172deg, #e4d5c8 0%, #efe2d6 12%, var(--sepia-light) 30%, #f1e5da 55%, #d9c2af 72%, #6e5443 88%, #3a2a1f 100%);
  }
  .title {
    position: absolute;
    top: 472px; left: 130px;
    width: 640px;
    font-family: "Special Elite", monospace;
    font-weight: 400;
    font-size: 70px;
    line-height: 78px;
    color: var(--type-ink);
    transform: rotate(9deg);
    transform-origin: left top;
  }
  .title-line { display: block; white-space: nowrap; }
  .title-line--second { margin-left: -40px; }
  .publisher-band {
    position: absolute;
    top: 1110px; left: 0;
    width: 820px;
    height: 90px;
    background: var(--footer-band);
    display: flex;
    align-items: center;
    justify-content: center;
  }
  .publisher-name {
    font-family: "Lato", sans-serif;
    font-weight: 400;
    font-size: 38px;
    color: var(--ink-black);
  }
</style>
</head>
<body>
  <main class="cover">
    <header class="author-band">
      <p class="author-name">Luc Dorvasse</p>
    </header>

    <div class="typewriter-photo" role="img" aria-label="Gros plan sépia d'une machine à écrire, feuille engagée sous la règle graduée, barres de caractères floues au premier plan"></div>

    <h1 class="title">
      <span class="title-line">Le veilleur</span>
      <span class="title-line title-line--second">et la rive</span>
    </h1>

    <footer class="publisher-band">
      <p class="publisher-name">Editions Plumeaux</p>
    </footer>
  </main>
</body>
</html>
```